body balm label design

body balm tube design, current label design for other similar products
Need to have a design which can interchange between 3 different solutions
Amber Tide (Lavender + Vanilla)
Copper Harbor (Eucalyptus + Mint)
Velvet Arc (Bergamot + Cedarwood)
Tube size:
2.5h x 3.25 w
Target Market(s)
natural, solution focused
Requirements
Must have
- relatable to existing brand designs, focus on features and benefits

```html
<!DOCTYPE html>
<html lang="en">
<head>
<meta charset="utf-8">
<title>Amber Tide Body Balm Label</title>
<link rel="stylesheet" href="https://fonts.googleapis.com/css2?family=Montserrat:wght@400;500&family=Playfair+Display:wght@500&family=Cormorant+Garamond:ital,wght@0,400;0,500;1,400&family=Parisienne&display=swap">
<style>
  :root {
    --teal: #357f7c;
    --teal-deep: #2a6b68;
    --label: #f4f4f2;
    --backdrop: #e6e6e6;
    --rule: #9bbcba;
    --white: #ffffff;
  }
  * { margin: 0; padding: 0; box-sizing: border-box; }
  html, body { width: 1200px; height: 1001px; overflow: hidden; background: var(--backdrop); }
  .canvas { position: relative; width: 1200px; height: 1001px; }

  .label-panel {
    position: absolute; top: 120px; width: 300px; height: 760px;
    background: var(--label); overflow: hidden;
    box-shadow: 0 2px 10px rgba(0,0,0,0.06);
  }
  .label-front { left: 220px; }
  .label-back { left: 680px; }

  /* front */
  .feature-block {
    position: absolute; left: 28px; top: 130px; width: 178px; height: 520px;
    background: var(--teal); border-bottom-left-radius: 178px 190px;
    color: var(--white); text-align: center;
  }
  .product-type {
    margin-top: 30px; font-family: "Montserrat", sans-serif; font-weight: 500;
    font-size: 19px; letter-spacing: 6px; line-height: 31px; padding-left: 6px;
  }
  .scent-line {
    margin: 12px auto 0; width: 120px; padding: 5px 0;
    border-top: 1px solid rgba(255,255,255,0.7); border-bottom: 1px solid rgba(255,255,255,0.7);
    font-family: "Cormorant Garamond", serif; font-style: italic; font-size: 12px; letter-spacing: 0.5px;
  }
  .origin-seal {
    position: absolute; left: 10px; top: 150px; width: 64px;
    font-family: "Cormorant Garamond", serif; line-height: 1.05; text-align: center;
  }
  .origin-seal .small { font-size: 8px; letter-spacing: 1px; }
  .origin-seal .big { font-size: 13px; }
  .botanical-art {
    position: absolute; left: 40px; top: 160px; width: 130px; height: 340px;
    background: linear-gradient(180deg, rgba(255,255,255,0.05), rgba(255,255,255,0.12));
    border-radius: 60px 60px 0 60px;
  }
  .product-name {
    position: absolute; left: 212px; top: 650px; width: 520px;
    transform: rotate(-90deg); transform-origin: 0 0;
    font-family: "Playfair Display", serif; font-weight: 500; font-size: 74px;
    line-height: 80px; color: var(--teal); text-transform: uppercase; white-space: nowrap;
    letter-spacing: 1px;
  }
  .net-weight {
    position: absolute; left: 0; right: 0; top: 696px; text-align: center;
    font-family: "Montserrat", sans-serif; font-size: 13px; font-weight: 500; color: var(--teal-deep);
  }

  /* back */
  .back-layout {
    position: absolute; width: 760px; height: 300px; left: -230px; top: 230px;
    transform: rotate(-90deg); color: var(--teal-deep);
    padding: 14px 40px 0 40px;
  }
  .value-row {
    display: flex; align-items: center; gap: 18px; justify-content: center;
    font-family: "Parisienne", cursive; font-size: 30px; color: var(--teal); height: 56px;
  }
  .value-row .dash { width: 60px; height: 1px; background: var(--teal); }
  .ingredients {
    margin-top: 8px; text-align: center; font-family: "Cormorant Garamond", serif;
    font-size: 13px; line-height: 17px; color: var(--teal-deep);
  }
  .ingredients-title { display: block; }
  .back-rule { margin: 16px 0 0; height: 1px; background: var(--rule); }
  .contact-row {
    display: flex; align-items: center; justify-content: space-between; margin-top: 16px;
    font-family: "Cormorant Garamond", serif; font-size: 12px; letter-spacing: 0.3px;
  }
  .contact-row .site { letter-spacing: 1px; }
  .social-dots { display: flex; gap: 10px; }
  .social-dots span { width: 24px; height: 24px; border-radius: 50%; background: var(--teal); display: block; }
</style>
</head>
<body>
<div class="canvas">

  <section class="label-panel label-front">
    <div class="feature-block">
      <div class="product-type">BODY<br>BALM</div>
      <div class="scent-line">LAVENDER + VANILLA</div>
      <div class="botanical-art" role="img" aria-label="Fine white line drawing of lavender sprigs"></div>
      <div class="origin-seal">
        <div class="small">MADE IN</div>
        <div class="big">100%</div>
        <div class="small">NATURAL</div>
        <div class="small">CANADA</div>
      </div>
    </div>
    <div class="product-name">Amber Tide</div>
    <div class="net-weight">Net Wt. 0.5oz / 14 g</div>
  </section>

  <section class="label-panel label-back">
    <div class="back-layout">
      <div class="value-row">
        <span>plant based</span><span class="dash"></span>
        <span>vegan</span><span class="dash"></span>
        <span>cruelty free</span>
      </div>
      <p class="ingredients">
        <span class="ingredients-title">Ingredients:</span>
        Organic Olive Fruit Oil (Olea Europaea), Organic Coconut Oil (Cocos Nucifera), Organic Shea Butter (Butyrospermum Parkii), Organic Jojoba Seed Oil (Simmondsia Chinensis), Rosehip Seed Oil (Rosa Canina), Vitamin E (Tocopherol), Sunflower Seed Oil (Helianthus Annuus), Vanilla Aroma, Mentha Piperita (Peppermint) Leaf Oil, Dipteryx Odorata (Tonka Bean) Oil
      </p>
      <div class="back-rule"></div>
      <div class="contact-row">
        <span class="site">WWW.HOLLOWFERN.CA</span>
        <span>Made by Hollow Fern, Brightwater, AB T0X 2B4</span>
        <span class="social-dots"><span></span><span></span><span></span></span>
      </div>
    </div>
  </section>

</div>
</body>
</html>
```